Private Equity Company Stationary
business card, letterhead, envelope, fax cover
#46 please eliminate the email address from the envelope. Thanks
#34 Birchway Holdings Group Header and remove big logo/watermark from the center of the page.
#33 remove all the phone numbers from envelope
#21 please eliminate border (header and footer) from business card, letterhead, fax coverand just leave it plain. Please re-submit with changes
envelope flaps to remain white
The only place the cell phone number is needed is on the business card.
I need some clarification before I can submit a satifactory design.
1. Do we need to mention the name "Holdings Grouup Advisory, Inc." compulsarily in any of the media.
2. Are there any limitations on the no of colours that can be used as printing costs can vary significantly.

```html
<!DOCTYPE html>
<html lang="en">
<head>
<meta charset="utf-8">
<title>Birchway Holdings Group — Business Card</title>
<link href="https://fonts.googleapis.com/css2?family=Tinos:wght@400&display=swap" rel="stylesheet">
<style>
  :root {
    --page-bg: #ffffff;
    --card-white: #ffffff;
    --card-olive: #7d6e55;
    --ink: #2a2a2a;
    --brand-navy: #1f3a6e;
    --brand-bronze: #8a7757;
    --link-blue: #2f4f9a;
    --card-edge: #c9c9c9;
  }
  html, body {
    margin: 0;
    padding: 0;
    width: 1200px;
    height: 871px;
    overflow: hidden;
    background: var(--page-bg);
    font-family: "Tinos", "Times New Roman", serif;
  }
  .canvas {
    position: relative;
    width: 1200px;
    height: 871px;
  }
  .card {
    position: absolute;
    top: 281px;
    width: 540px;
    height: 309px;
    box-sizing: border-box;
  }
  .card--front {
    left: 40px;
    background: var(--card-white);
    border: 1px solid var(--card-edge);
    color: var(--ink);
  }
  .card--back {
    left: 620px;
    background: var(--card-olive);
  }
  .holder {
    position: absolute;
    left: 26px;
    top: 26px;
    font-size: 14px;
    line-height: 18px;
    margin: 0;
  }
  .brand {
    position: absolute;
    left: 150px;
    top: 128px;
    display: flex;
    align-items: center;
    gap: 12px;
  }
  .brand__square {
    width: 30px;
    height: 30px;
    background: var(--brand-bronze);
  }
  .brand__name {
    font-size: 21px;
    letter-spacing: 0.5px;
    color: var(--brand-navy);
    text-transform: uppercase;
    white-space: nowrap;
  }
  .contact {
    position: absolute;
    left: 233px;
    top: 201px;
    margin: 0;
    font-size: 12.5px;
    line-height: 21px;
    font-style: normal;
    white-space: nowrap;
  }
  .contact__web {
    color: var(--link-blue);
  }
  .brand--reverse {
    left: 50%;
    top: 50%;
    transform: translate(-50%, -50%);
  }
  .brand--reverse .brand__square {
    background: var(--card-white);
  }
  .brand--reverse .brand__name {
    color: var(--card-white);
  }
</style>
</head>
<body>
  <main class="canvas">
    <section class="card card--front" aria-label="Business card front">
      <p class="holder">Daniel Valmorent | Managing Director<br>Cell :(310) 555-0147</p>
      <div class="brand">
        <span class="brand__square"></span>
        <span class="brand__name">Birchway Holdings Group</span>
      </div>
      <address class="contact">
        418 W Fern Ave&nbsp; Suite 804&nbsp; Los Angeles, CA 90017<br>
        Toll free : (310) 555-0182 | Fax (310) 555-0169<br>
        Email: daniel@birchwayhg.com | <span class="contact__web">www.birchwayhg.com</span>
      </address>
    </section>
    <section class="card card--back" aria-label="Business card back">
      <div class="brand brand--reverse">
        <span class="brand__square"></span>
        <span class="brand__name">Birchway Holdings Group</span>
      </div>
    </section>
  </main>
</body>
</html>
```